Business Card

We need a business card for a fundraising/sales and marketing company called Kelvora Appeals services. The logo colours are Red Black and white. The final design should communicate professional, reliable yet fun and charity minded
Updates

Sorry for the delay. A decision will be made in the next 48 hours. we are stuck between two designs. Kind Regards, Molly Ravenscroft

Industry/Entity Type

Marketing

```html
<!DOCTYPE html>
<html lang="en">
<head>
<meta charset="utf-8">
<title>Kelvora Appeals – Business Card</title>
<link rel="stylesheet" href="https://fonts.googleapis.com/css2?family=Lato:wght@400;700;900&display=swap">
<style>
  :root {
    --backdrop: #2b2b2b;
    --card-white: #ffffff;
    --card-shade: #ececec;
    --brand-red: #d71f26;
    --ink-dark: #3a3a3a;
    --ink-mid: #555555;
    --tab-dark: #3d3d3d;
  }
  * { margin: 0; padding: 0; box-sizing: border-box; }
  html, body {
    width: 1200px; height: 900px; overflow: hidden;
    background: var(--backdrop);
    font-family: "Lato", Arial, sans-serif;
  }
  .business-card {
    position: absolute;
    left: 150px; top: 193px;
    width: 900px; height: 514px;
    background: radial-gradient(ellipse at 45% 35%, var(--card-white) 40%, var(--card-shade) 100%);
    overflow: hidden;
  }
  .brand {
    position: absolute;
    top: 150px; left: 0; width: 100%;
    display: flex; justify-content: center; align-items: center; gap: 14px;
  }
  .brand-dot {
    width: 22px; height: 22px; border-radius: 50%;
    background: var(--brand-red);
  }
  .brand-name {
    font-weight: 900; font-size: 46px; letter-spacing: 2px;
    color: var(--brand-red); text-transform: uppercase;
  }
  .person {
    position: absolute; left: 70px; top: 330px;
    text-transform: uppercase;
  }
  .person-name {
    font-weight: 900; font-size: 30px; color: var(--brand-red); line-height: 1.1;
  }
  .person-role {
    font-weight: 700; font-size: 24px; color: var(--ink-dark); line-height: 1.2;
  }
  .divider {
    position: absolute; left: 450px; top: 245px;
    width: 4px; height: 130px;
    background: linear-gradient(to bottom, rgba(215,31,38,0) 0%, var(--brand-red) 30%, var(--brand-red) 60%, rgba(215,31,38,0) 100%);
    transform: rotate(-12deg);
  }
  .contact-list {
    position: absolute; left: 500px; top: 240px;
    list-style: none;
  }
  .contact-item {
    display: flex; align-items: center; gap: 12px;
    font-size: 22px; color: var(--ink-dark); line-height: 40px;
  }
  .contact-icon { width: 22px; height: 22px; flex: none; }
  .card-edge { position: absolute; left: 0; bottom: 0; width: 900px; height: 60px; }
</style>
</head>
<body>
  <section class="business-card">
    <div class="brand">
      <span class="brand-dot"></span>
      <span class="brand-name">Kelvora Appeals</span>
    </div>

    <div class="person">
      <p class="person-name">Molly Ravenscroft</p>
      <p class="person-role">Managing Director</p>
    </div>

    <div class="divider"></div>

    <ul class="contact-list">
      <li class="contact-item">
        <svg class="contact-icon" viewBox="0 0 24 24"><path fill="#d71f26" d="M3 9c0-3 4-5 9-5s9 2 9 5l-3 2-3-2V7H9v2l-3 2zM6 12h12l2 8H4z"/><circle cx="12" cy="16" r="2" fill="#fff"/></svg>
        <span>0400 555 013</span>
      </li>
      <li class="contact-item">
        <svg class="contact-icon" viewBox="0 0 24 24"><rect x="2" y="5" width="20" height="14" fill="#d71f26"/><path d="M2 5l10 8 10-8" fill="none" stroke="#fff" stroke-width="2"/></svg>
        <span>molly@kelvoraappeals.com</span>
      </li>
      <li class="contact-item">
        <svg class="contact-icon" viewBox="0 0 24 24"><g fill="none" stroke="#d71f26" stroke-width="2.5"><rect x="3" y="10" width="9" height="5" rx="2.5" transform="rotate(-45 7.5 12.5)"/><rect x="12" y="9" width="9" height="5" rx="2.5" transform="rotate(-45 16.5 11.5)"/></g></svg>
        <span>www.kelvoraappeals.com</span>
      </li>
    </ul>

    <svg class="card-edge" viewBox="0 0 900 60" preserveAspectRatio="none">
      <path d="M0 42 L560 42 Q580 42 590 52 L600 60 L0 60 Z" fill="var(--brand-red)"/>
      <path d="M560 42 Q585 14 620 14 L900 14 L900 60 L600 60 Q590 50 560 42 Z" fill="var(--tab-dark)"/>
    </svg>
  </section>
</body>
</html>
```